The Lantern Den Business Cards

We are a Craft Beer/Upscale dining Bar/Restaurant. We'll have 24 taps of craft beers and several types of bottled beers. In addition, we'll be serving a variety of top shelf bourbons, spirits and wines with a small unique menu. I'd like the design to be sophisticated, elegant and modern while staying away from "cartoonish" pictures.
Updates
Hello, I've added some example logos for inspiration. I'd like to use a lot of black/white with maybe a little color for a "pop". Thank you!
Industry/Entity Type
Business
Contact Information for Business Card
THE LANTERN DEN
Tomas Orlikova
582 Wexmoor Street
Harlow Bay, Westmere 23847
Office: (555) 555-0143
Mobile: (555) 555-0178
Look and feel
Each slider illustrates characteristics of the customer's brand and the style your logo design should communicate.

```html
<!DOCTYPE html>
<html lang="en">
<head>
<meta charset="utf-8">
<title>The Lantern Den – Business Card</title>
<link rel="stylesheet" href="https://fonts.googleapis.com/css2?family=Lato:wght@400;900&display=swap">
<style>
  :root {
    --page-bg: #e9e6e1;
    --frost-light: #f4f5f7;
    --frost-mid: #dfe2e6;
    --frost-blush: #e9d6d9;
    --panel-dark: #0b0f16;
    --panel-edge: #1c2230;
    --accent-gold: #cdb894;
    --accent-soft: #d9ccb2;
    --wordmark: #363a40;
    --rim-light: #e8e2d6;
    --rim-dark: #7c6a52;
  }
  * { margin: 0; padding: 0; box-sizing: border-box; }
  html, body {
    width: 1200px;
    height: 970px;
    overflow: hidden;
    background: var(--page-bg);
    font-family: "Lato", Arial, sans-serif;
  }
  .business-card {
    position: absolute;
    left: 100px;
    top: 208px;
    width: 1000px;
    height: 554px;
    box-shadow: 0 18px 40px rgba(0, 0, 0, 0.22);
  }
  .card-art {
    position: absolute;
    inset: 0;
    width: 100%;
    height: 100%;
    display: block;
  }
  .wordmark {
    position: absolute;
    left: 0;
    width: 446px;
    top: 132px;
    text-align: center;
    color: var(--wordmark);
    font-weight: 900;
    font-size: 48px;
    line-height: 83px;
    letter-spacing: 4px;
  }
  .contact-name {
    position: absolute;
    left: 622px;
    top: 62px;
    font-size: 32px;
    color: var(--accent-soft);
    font-weight: 400;
  }
  .contact-address {
    position: absolute;
    left: 563px;
    top: 218px;
    font-size: 26px;
    line-height: 40px;
    color: var(--accent-gold);
    font-style: normal;
  }
  .contact-phones {
    position: absolute;
    left: 606px;
    top: 396px;
    list-style: none;
    font-size: 26px;
    color: var(--accent-gold);
  }
  .contact-phones li {
    display: flex;
    align-items: center;
    height: 50px;
  }
  .phone-icon {
    width: 26px;
    height: 26px;
    margin-right: 29px;
    fill: var(--accent-gold);
  }
</style>
</head>
<body>
  <main class="business-card">
    <svg class="card-art" viewBox="0 0 1000 554" preserveAspectRatio="none" aria-hidden="true">
      <defs>
        <linearGradient id="frost" x1="0" y1="0" x2="0.3" y2="1">
          <stop offset="0" stop-color="var(--frost-mid)"/>
          <stop offset="0.45" stop-color="var(--frost-light)"/>
          <stop offset="0.8" stop-color="var(--frost-blush)"/>
          <stop offset="1" stop-color="var(--frost-mid)"/>
        </linearGradient>
        <linearGradient id="panel" x1="0" y1="0" x2="1" y2="1">
          <stop offset="0" stop-color="var(--panel-dark)"/>
          <stop offset="0.7" stop-color="var(--panel-dark)"/>
          <stop offset="1" stop-color="var(--panel-edge)"/>
        </linearGradient>
        <linearGradient id="rim" x1="0" y1="0" x2="0" y2="1">
          <stop offset="0" stop-color="var(--rim-dark)"/>
          <stop offset="0.45" stop-color="var(--rim-light)"/>
          <stop offset="1" stop-color="var(--rim-dark)"/>
        </linearGradient>
      </defs>
      <rect class="frost-side" width="1000" height="554" fill="url(#frost)"/>
      <path class="rim-curve" d="M429 0 Q578 277 422 554 L414 554 Q552 277 424 0 Z" fill="url(#rim)"/>
      <path class="dark-panel" d="M429 0 Q578.5 277 422 554 H1000 V0 Z" fill="url(#panel)"/>
    </svg>

    <h1 class="wordmark">THE<br>LANTERN<br>DEN</h1>

    <p class="contact-name">Tomas Orlikova</p>

    <address class="contact-address">582 Wexmoor Street Harlow Bay,<br>Westmere 23847</address>

    <ul class="contact-phones">
      <li class="phone-mobile">
        <svg class="phone-icon" viewBox="0 0 24 24" aria-label="Mobile"><path d="M7 1h10a2 2 0 0 1 2 2v18a2 2 0 0 1-2 2H7a2 2 0 0 1-2-2V3a2 2 0 0 1 2-2zm0 3v14h10V4H7zm5 15.5a1 1 0 1 0 0 2 1 1 0 0 0 0-2z"/></svg>
        (555) 555-0178
      </li>
      <li class="phone-office">
        <svg class="phone-icon" viewBox="0 0 24 24" aria-label="Office"><path d="M2 8c0-2 4-4 10-4s10 2 10 4v2h-5V8c-1-.6-3-1-5-1s-4 .4-5 1v2H2V8zm4 4h12l3 8H3l3-8zm6 1.5a2.5 2.5 0 1 0 0 5 2.5 2.5 0 0 0 0-5z"/></svg>
        (555) 555-0143
      </li>
    </ul>
  </main>
</body>
</html>
```